NFC (Near field communication) - Business Card Design

IT/ Telecom:

We would like a new business card that contains our logo, contact info for the company and contact info for the owner. We also wolud like to be innovative, and create NFC technology inside the card.

This means that mobile phones can be placed on the card, and the contactinfo automaticly stores into the phonebook. Therefore, a cirkle or similar - with the text: "Place your phone here!" (please write it in Norwagian): "Aktiver NFC og legg mobilen din her!".

Please google NFC or near field communication and use your imagination on the design as we love surprises :-)

Industry/Entity Type

Communication

Requirements
Must have
• Text: "Activate NFC on your phone and place your mobile here - in Norwegian: "Aktiver NFC og legg mobilen din her!".
Nice to have
• Please see attachment #5 for inspiration.

```html
<!DOCTYPE html>
<html lang="en">
<head>
<meta charset="utf-8">
<title>linkwave – NFC business card</title>
<link href="https://fonts.googleapis.com/css2?family=Arimo:wght@400;700&display=swap" rel="stylesheet">
<style>
  :root {
    --page-bg: #e9ecef;
    --card-light: #eef3f7;
    --card-mid: #d3dee7;
    --card-deep: #b7c8d6;
    --arc-light: rgba(255,255,255,0.55);
    --arc-soft: rgba(255,255,255,0.28);
    --band: rgba(150,175,195,0.35);
    --ink: #2f6f8c;
    --ink-soft: #4a7f98;
  }
  * { margin: 0; padding: 0; box-sizing: border-box; }
  html, body { width: 1200px; height: 900px; overflow: hidden; }
  body {
    background: var(--page-bg);
    font-family: "Arimo", Arial, sans-serif;
    color: var(--ink);
    position: relative;
  }
  .card {
    position: absolute;
    left: 250px;
    width: 700px;
    height: 400px;
    overflow: hidden;
    background: linear-gradient(160deg, var(--card-light) 0%, var(--card-mid) 55%, var(--card-deep) 100%);
    box-shadow: 0 6px 18px rgba(40,60,80,0.18);
  }
  .card-front { top: 40px; }
  .card-back { top: 470px; }
  .card-arcs { position: absolute; inset: 0; width: 100%; height: 100%; }

  /* front */
  .nfc-zone {
    position: absolute;
    left: 0; right: 0; top: 120px;
    display: flex; align-items: center; justify-content: center; gap: 18px;
  }
  .brand-square {
    width: 70px; height: 52px;
    background: var(--ink);
    border-radius: 10px;
  }
  .brand-name {
    font-size: 44px;
    font-weight: 400;
    color: var(--ink);
    letter-spacing: 0.5px;
  }
  .nfc-prompt {
    position: absolute;
    left: 0; right: 0; top: 232px;
    text-align: center;
    font-size: 22px;
    letter-spacing: 3px;
  }

  /* back */
  .back-brand {
    position: absolute;
    left: 34px; top: 26px;
    display: flex; align-items: center; gap: 16px;
  }
  .back-brand .brand-square { width: 84px; height: 60px; }
  .back-brand .brand-name { font-size: 56px; }
  .holder {
    position: absolute;
    left: 300px; top: 168px;
  }
  .holder-name { font-size: 22px; letter-spacing: 3.5px; }
  .holder-role { font-size: 16px; letter-spacing: 2px; color: var(--ink-soft); margin-top: 4px; }
  .address {
    position: absolute;
    left: 40px; top: 286px;
    font-size: 15px; font-style: normal; line-height: 1.45; letter-spacing: 1.5px;
    color: var(--ink-soft);
  }
  .contact {
    position: absolute;
    left: 300px; top: 270px;
    display: grid;
    grid-template-columns: 88px auto;
    row-gap: 4px;
    font-size: 17px; letter-spacing: 2px;
  }
  .contact dt { color: var(--ink-soft); }
</style>
</head>
<body>

<section class="card card-front" aria-label="Card front with NFC touch area">
  <svg class="card-arcs" viewBox="0 0 700 400" preserveAspectRatio="none" aria-hidden="true">
    <path d="M0 40 C 180 30 320 120 420 400 L0 400 Z" fill="var(--arc-soft)"/>
    <path d="M0 340 C 200 120 480 60 700 70 L700 0 L0 0 Z" fill="var(--arc-light)"/>
    <path d="M0 400 C 220 190 480 130 700 140" fill="none" stroke="rgba(255,255,255,0.6)" stroke-width="2"/>
  </svg>
  <div class="nfc-zone">
    <div class="brand-square"></div>
    <span class="brand-name">linkwave</span>
  </div>
  <p class="nfc-prompt">Aktiver NFC og legg mobilen din her</p>
</section>

<section class="card card-back" aria-label="Card back with contact details">
  <svg class="card-arcs" viewBox="0 0 700 400" preserveAspectRatio="none" aria-hidden="true">
    <rect x="0" y="0" width="700" height="120" fill="var(--band)"/>
    <path d="M0 260 C 200 120 460 90 700 100 L700 0 L0 0 Z" fill="var(--arc-light)"/>
    <path d="M0 400 C 80 260 200 180 380 150 C 500 130 620 125 700 128 L700 400 Z" fill="var(--arc-soft)"/>
    <path d="M0 250 C 200 140 460 112 700 118" fill="none" stroke="rgba(255,255,255,0.7)" stroke-width="2"/>
  </svg>
  <div class="back-brand">
    <div class="brand-square"></div>
    <span class="brand-name">linkwave</span>
  </div>
  <div class="holder">
    <p class="holder-name">RK NORDLINE</p>
    <p class="holder-role">Designer</p>
  </div>
  <address class="address">
    Address:<br>
    2207 Harbour Lane,<br>
    Some town, K4K4K4.
  </address>
  <dl class="contact">
    <dt>Phone:</dt><dd>01 2468 1357</dd>
    <dt>Email:</dt><dd>rknordline@linkwave.com</dd>
    <dt>Website:</dt><dd>www.linkwave.com</dd>
  </dl>
</section>

</body>
</html>
```